Delivery Company / Logistics Company Flyer

Im looking for something I can mail out to my current and potential customers highlighting our services, history, service locations, and contact information.(see uploaded DOC)
Website: http://www.kalvontransit.com/
About:
• 35 years in the delivery business Kalvon provides a custom logistics solution to each customer’s needs. Led by an experienced leadership group and a very versatile operations team Kalvon Provides the “boutique” solution to their customers’ vs. The cookie cutter service the majority of the industry provides.
Assets:
• We have a tremendous group of drivers operating over 100 assets ranging from Courier Vans to 53ft Tractor trailers.
Markets Serviced:
• Dallas TX
• Kansas City MO
• St. Louis MO
Services:
• White Glove Deliveries
• Home Delivery
• B2B
• B2C
• Airport Transfers
• Cross dock and Warehousing Logistics
• Courier Deliveries
• Pharmaceutical Deliveries
• Dedicated Services
Associations:
• BFX Certified Carrier
• Green Route Haulage Partner
• NMU (national movers union)
Contact information:
Dean Marwick – Sales
Mobile: 940.555.0186
Email: dmarwick@kvtx.example and sales@kvtx.example
Target Market(s)
Shipping companies in Dallas TX, Kansas City MO and St. Louis MO.(see uploaded DOC)
Industry/Entity Type
Trucking Company
Requirements
Must have
- Points on the US map where we service Dallas TX, Kansas City MO and St. Louis MO. Contact info, services we proved, assets, brief history.(see uploaded DOC)
Nice to have
- Associations (see uploaded DOC)

```html
<!DOCTYPE html>
<html lang="en">
<head>
<meta charset="utf-8">
<title>Kalvon Logistics – Flyer</title>
<link href="https://fonts.googleapis.com/css2?family=Bebas+Neue&family=Montserrat:wght@400;700;800&display=swap" rel="stylesheet">
<style>
  :root{
    --yellow:#f5d31c;
    --ink:#2b2b2b;
    --black:#0a0a0a;
    --paper:#ffffff;
    --cream:#f6e6cf;
    --backdrop:#c4c4c4;
  }
  *{box-sizing:border-box;margin:0;padding:0}
  html,body{width:941px;height:1200px;overflow:hidden;background:var(--backdrop)}
  .flyer{position:absolute;left:46px;top:0;width:848px;height:1200px;background:var(--paper);overflow:hidden;font-family:"Montserrat",sans-serif;color:var(--ink)}
  .abs{position:absolute}
  .brand{left:45px;top:98px;font-weight:800;color:var(--black);font-size:56px;line-height:60px;letter-spacing:-1px}
  .tagline{left:43px;top:276px;font-size:32px;font-weight:400;color:var(--ink)}
  .headline{left:43px;top:318px;font-family:"Bebas Neue",sans-serif;font-size:62px;line-height:56px;color:var(--yellow)}
  .hero{left:384px;top:38px;width:464px;height:449px;background:radial-gradient(ellipse at 60% 50%,#d2d2d2 0%,#b9b9b9 40%,#f0f0f0 75%,#fff 100%)}
  .bands{left:0;top:430px;width:848px;height:570px}
  .pill{height:44px;border-radius:0 22px 22px 0;background:var(--ink);color:#fff;font-weight:800;font-size:24px;display:flex;align-items:center;padding-left:46px}
  .pill.services{background:var(--yellow);color:var(--black);padding-left:30px}
  .copy{left:47px;font-size:14.4px;line-height:20.4px;color:var(--ink);white-space:nowrap}
  .service-list{left:462px;top:540px;list-style:none}
  .service-list li{display:flex;align-items:flex-start;gap:20px;color:#fff;font-weight:700;font-size:20px;line-height:26px;margin-bottom:11px}
  .service-list svg{flex:none;margin-top:2px}
  .assoc-title{left:46px;top:976px;font-weight:800;font-size:18px;line-height:22px}
  .assoc-list{left:46px;top:1014px;list-style:none}
  .assoc-list li{display:flex;align-items:center;gap:10px;font-weight:700;font-size:15.5px;line-height:27px}
  .coverage-back{left:560px;top:972px;width:288px;height:228px;background:var(--yellow)}
  .coverage{left:512px;top:914px;width:284px;height:266px;transform:rotate(3deg);background:linear-gradient(135deg,#fafaf5,#e9e6dc);box-shadow:0 4px 12px rgba(0,0,0,.35)}
  .footer{left:0;top:1104px;width:545px;height:96px}
  .call{left:45px;top:1112px;font-weight:800;font-size:24px;line-height:30px;color:var(--yellow)}
  .phone{left:45px;top:1142px;display:flex;align-items:center;gap:8px;font-family:"Bebas Neue",sans-serif;font-size:58px;line-height:56px;color:var(--cream)}
  .mail{left:348px;top:1117px;width:140px;text-align:center;color:#e8e8e8;font-size:13.5px;line-height:20px}
  .mail-icon{display:block;margin:0 auto 8px}
</style>
</head>
<body>
<div class="flyer">
  <div class="abs brand">Kalvon<br>Logistics</div>
  <div class="abs hero" role="img" aria-label="Photo of a smiling delivery driver carrying a branded cardboard box in front of a white semi truck"></div>
  <div class="abs tagline">It’s Just Like Having</div>
  <div class="abs headline">YOUR OWN FLEET....<br>EXCEPT IT’S OURS</div>

  <svg class="abs bands" viewBox="0 0 848 570" aria-hidden="true">
    <defs>
      <linearGradient id="darkFade" x1="0" y1="0" x2="0" y2="1">
        <stop offset="0" stop-color="#444"/><stop offset="1" stop-color="#000"/>
      </linearGradient>
    </defs>
    <polygon fill="var(--yellow)" points="0,30 40,26 80,32 120,24 160,28 200,22 240,30 280,24 320,27 360,22 400,30 431,28 431,545 0,545"/>
    <polygon fill="url(#darkFade)" points="431,34 470,26 510,22 550,20 590,16 630,18 670,12 710,10 750,12 790,6 820,8 848,4 848,545 431,545"/>
    <polygon fill="#fff" points="0,541 60,536 120,543 180,537 240,543 300,535 360,541 431,540 480,536 540,530 600,534 660,528 700,534 700,570 0,570"/>
  </svg>

  <div class="abs pill" style="left:0;top:482px;width:179px">About:</div>
  <p class="abs copy" style="top:545px">35 years in the delivery business Kalvon provides<br>a custom logistics solution to each customer’s<br>needs. Led by an experienced leadership group<br>and a very versatile operations team Kalvon Pro-<br>vides the “boutique” solution to their customers’<br>vs.&nbsp; The cookie cutter service the majority of the<br>industry provides</p>
  <div class="abs pill" style="left:0;top:711px;width:179px">Assets:</div>
  <p class="abs copy" style="top:768px">We have a tremendous group of drivers oper-<br>ating over 100 assets ranging from Courier<br>Vans to 53ft Tractor trailers.</p>
  <div class="abs pill" style="left:0;top:843px;width:312px;padding-left:43px">Markets Serviced:</div>
  <p class="abs copy" style="top:899px">Dallas TX<br>Kansas City MO<br>St. Louis MO</p>

  <div class="abs pill services" style="left:431px;top:482px;width:255px">Services:</div>
  <ul class="abs service-list">
    <li><svg width="20" height="20" viewBox="0 0 20 20"><circle cx="10" cy="10" r="8" fill="none" stroke="var(--yellow)" stroke-width="2"/><path d="M6 10l3 3 8-9" fill="none" stroke="var(--yellow)" stroke-width="2.4"/></svg>White Glove Deliveries</li>
    <li><svg width="20" height="20" viewBox="0 0 20 20"><circle cx="10" cy="10" r="8" fill="none" stroke="var(--yellow)" stroke-width="2"/><path d="M6 10l3 3 8-9" fill="none" stroke="var(--yellow)" stroke-width="2.4"/></svg>Home Delivery</li>
    <li><svg width="20" height="20" viewBox="0 0 20 20"><circle cx="10" cy="10" r="8" fill="none" stroke="var(--yellow)" stroke-width="2"/><path d="M6 10l3 3 8-9" fill="none" stroke="var(--yellow)" stroke-width="2.4"/></svg>B2B</li>
    <li><svg width="20" height="20" viewBox="0 0 20 20"><circle cx="10" cy="10" r="8" fill="none" stroke="var(--yellow)" stroke-width="2"/><path d="M6 10l3 3 8-9" fill="none" stroke="var(--yellow)" stroke-width="2.4"/></svg>B2C</li>
    <li><svg width="20" height="20" viewBox="0 0 20 20"><circle cx="10" cy="10" r="8" fill="none" stroke="var(--yellow)" stroke-width="2"/><path d="M6 10l3 3 8-9" fill="none" stroke="var(--yellow)" stroke-width="2.4"/></svg>Airport Transfers</li>
    <li><svg width="20" height="20" viewBox="0 0 20 20"><circle cx="10" cy="10" r="8" fill="none" stroke="var(--yellow)" stroke-width="2"/><path d="M6 10l3 3 8-9" fill="none" stroke="var(--yellow)" stroke-width="2.4"/></svg>Cross dock and<br>Warehousing&nbsp; Logistics</li>
    <li><svg width="20" height="20" viewBox="0 0 20 20"><circle cx="10" cy="10" r="8" fill="none" stroke="var(--yellow)" stroke-width="2"/><path d="M6 10l3 3 8-9" fill="none" stroke="var(--yellow)" stroke-width="2.4"/></svg>Courier Deliveries</li>
    <li><svg width="20" height="20" viewBox="0 0 20 20"><circle cx="10" cy="10" r="8" fill="none" stroke="var(--yellow)" stroke-width="2"/><path d="M6 10l3 3 8-9" fill="none" stroke="var(--yellow)" stroke-width="2.4"/></svg>Pharmaceutical Deliveries</li>
    <li><svg width="20" height="20" viewBox="0 0 20 20"><circle cx="10" cy="10" r="8" fill="none" stroke="var(--yellow)" stroke-width="2"/><path d="M6 10l3 3 8-9" fill="none" stroke="var(--yellow)" stroke-width="2.4"/></svg>Dedicated Services</li>
  </ul>

  <div class="abs coverage-back"></div>
  <div class="abs coverage" role="img" aria-label="Pinned note with a US map highlighting the central and eastern coverage area around Dallas TX, Kansas City MO and St. Louis MO, captioned Coverage Area in hand lettering"></div>

  <div class="abs assoc-title">Associations:</div>
  <ul class="abs assoc-list">
    <li><svg width="14" height="14" viewBox="0 0 14 14"><circle cx="7" cy="7" r="7" fill="var(--ink)"/><circle cx="7" cy="7" r="4.5" fill="none" stroke="var(--yellow)" stroke-width="1.3"/><path d="M4.6 7l1.8 1.8 3.4-3.6" fill="none" stroke="var(--yellow)" stroke-width="1.4"/></svg>BFX Certified Carrier</li>
    <li><svg width="14" height="14" viewBox="0 0 14 14"><circle cx="7" cy="7" r="7" fill="var(--ink)"/><circle cx="7" cy="7" r="4.5" fill="none" stroke="var(--yellow)" stroke-width="1.3"/><path d="M4.6 7l1.8 1.8 3.4-3.6" fill="none" stroke="var(--yellow)" stroke-width="1.4"/></svg>Green Route Haulage Partner</li>
    <li><svg width="14" height="14" viewBox="0 0 14 14"><circle cx="7" cy="7" r="7" fill="var(--ink)"/><circle cx="7" cy="7" r="4.5" fill="none" stroke="var(--yellow)" stroke-width="1.3"/><path d="M4.6 7l1.8 1.8 3.4-3.6" fill="none" stroke="var(--yellow)" stroke-width="1.4"/></svg>NMU (national movers union)</li>
  </ul>

  <svg class="abs footer" viewBox="0 0 545 96" aria-hidden="true">
    <path d="M0 0H500Q510 0 515 10L545 96H0Z" fill="var(--ink)"/>
  </svg>
  <div class="abs call">Call us Today!</div>
  <div class="abs phone">
    <svg width="20" height="20" viewBox="0 0 20 20" aria-hidden="true"><circle cx="10" cy="10" r="10" fill="var(--yellow)"/><path d="M8 5.5c-1.8 1-2.2 3.5-1 5.8s3.4 3.6 5.4 3.1l.8-1.8-2-1-1 .8c-.9-.5-1.6-1.5-1.9-2.5l.9-.8-.6-2.2z" fill="var(--ink)"/></svg>
    940.555.0186
  </div>
  <div class="abs mail">
    <svg class="mail-icon" width="24" height="24" viewBox="0 0 24 24" aria-hidden="true"><circle cx="12" cy="12" r="12" fill="var(--yellow)"/><rect x="6" y="8" width="12" height="8.5" fill="none" stroke="#fff" stroke-width="1.2"/><path d="M6 8l6 5 6-5" fill="none" stroke="#fff" stroke-width="1.2"/></svg>
    dmarwick@kvtx.example<br>sales@kvtx.example
  </div>
</div>
</body>
</html>
```